Swimming Pool Service business card needed!!!! Please

Hi Everyone! Thanks for looking at my contest. I PROMISE to provide excellent feedback during this process.

I am starting a new swimming pool cleaning business in San Diego, California and would like your help in making a business card for me.

I like easy to read, classy and sophisticated.

I am having a website designed and I'm looking for it to have pictures of really clean & clear pools.

I really like the blue on white color format, but open to other colors.

I do not have a logo, but the name of my company is GLIMMERTIDE POOL SERVICE.

My tag line is: Pools so clean, you can see yourself "in" them. (does not need to have the quotes around "in"...maybe just italics for this word IN?) You decide for me.

I would like to have a logo designed that incorporates some sort of easy to read letters. I do not want cursive (handwriting) letters. I thought about having a "reflection" of letters (mirror image), but think that this will be hard to read from far away. Maybe you can surprise me and come up with an idea that works using the a mirror image....but I'm not sure. I was leaning toward plain old BLOCK letters as I think it would be easy to read on my truck.

I would like to have the NAQTR and WBK logos on the back of the card. I have attached those two as files. You can put other things on the back as well, but I need these two logos on there. Or maybe put them on the front of the card if you have a better idea for the back of the card! :-)

Maybe blue on the back of the card and white on the front of the card? I don't know, I'm just thinking out loud.

I had another card done awhile ago called HARBORLINE TEES. I have uploaded a copy of that card for your reference. I don't want this card to be the same as my new company is a swimming pool cleaning company, but I wanted you to see what I liked in the past.

THANK YOU!!!!
Updates

Reason: Partner out of town and want their feedback....so need more time to decide and designs still coming in.

Industry/Entity Type

Business

Contact Information for Business Card

GLIMMERTIDE POOL SERVICE
Dale Wexby
Owner
4817 Quarry Bend Ave. #512
San Diego, CA 92417
858-291-6083
www.glimmertidepoolservice.example

Font styles to use
Sans Serif

Colors
0255a3
3176b5
ffffff

Requirements
Nice to have
• Some things to (possibly) add to back of card (in no particular order)
• WBK logo
• NAQTR logo
• Free Estimates
• Residential and Commercial Services
• Equipment Repairs
• Saltwater Systems
• Licensed, Bonded, Insured
• Family Owned and Operated
• No Contracts
• =======================
• Check out the FolioMint business card that i attached.
• i think they did this using a chrome overlay.
• Can any of you guys design that? or is that done at my printer?
• ==================
Should not have
• Hi Designers-
• The first round of cards came back and let's stay away from the light blue (powder blue) color. I don't like the look of it on the business cards.
• Also, the pool company JPG's that I attached are other logos of pool companies that I liked. I don't want them to be on my card. The only logos that should be on my card are the one you are going to come up with for my company, the WBK logo and the NAQTR logo.
• Lastly, no vertical cards and no split cards (logo on left, contact info on right side).
• Thanks much!

```html
<!DOCTYPE html>
<html lang="en">
<head>
<meta charset="utf-8">
<title>Glimmertide Pool Service – Business Card</title>
<link rel="stylesheet" href="https://fonts.googleapis.com/css2?family=Oswald:wght@600&family=Questrial&display=swap">
<style>
  :root {
    --paper: #ffffff;
    --deep-blue: #0255a3;
    --mid-blue: #3176b5;
    --text-light: #ffffff;
  }
  html, body {
    margin: 0;
    padding: 0;
    width: 1200px;
    height: 737px;
    overflow: hidden;
    background: var(--paper);
  }
  .business-card {
    display: block;
    width: 1200px;
    height: 737px;
  }
  .card-field { fill: var(--deep-blue); }
  .card-swoosh { fill: var(--paper); }
  .brand-name {
    font-family: "Oswald", "Arial Narrow", sans-serif;
    font-weight: 600;
    font-size: 92px;
    fill: var(--mid-blue);
  }
  .person-line,
  .contact-line {
    font-family: "Questrial", "Century Gothic", sans-serif;
    fill: var(--text-light);
  }
  .person-line { font-size: 31px; }
  .contact-line { font-size: 29px; text-anchor: end; }
</style>
</head>
<body>
<svg class="business-card" viewBox="0 0 1146 704" preserveAspectRatio="none" xmlns="http://www.w3.org/2000/svg">
  <rect class="card-field" x="30" y="38" width="1116" height="666"/>
  <path class="card-swoosh" d="M30,38 L810,38 C960,55 1100,120 1095,210 C1088,310 760,395 420,420 C250,440 70,442 46,402 C40,388 36,378 30,372 Z"/>

  <text class="brand-name" x="100" y="256" textLength="945" lengthAdjust="spacingAndGlyphs">GLIMMERTIDE POOL SERVICE</text>

  <g class="person-block">
    <text class="person-line" x="113" y="519">Dale Wexby</text>
    <text class="person-line" x="113" y="563">Owner</text>
  </g>

  <g class="contact-block">
    <text class="contact-line" x="1080" y="518">4817 Quarry Bend Ave. #512</text>
    <text class="contact-line" x="1080" y="554">San Diego, CA 92417</text>
    <text class="contact-line" x="1080" y="590">858-291-6083</text>
    <text class="contact-line" x="1080" y="628">www.glimmertidepoolservice.example</text>
  </g>
</svg>
</body>
</html>
```